Mental Health care Company in Washington DC

We are a new mental health care services provider in Washington DC. Please look at these sites.
https://marlowbrookpartners.com
https://www.quillstoneinc.com
https://velmarsh-kt.org/
https://www.trivanqx.com
https://www.thelanternofqz.com

```html
<!DOCTYPE html>
<html lang="en">
<head>
<meta charset="utf-8">
<title>Nerova Health Services</title>
<link href="https://fonts.googleapis.com/css2?family=Outfit:wght@300;400;500;600&display=swap" rel="stylesheet">
<style>
:root{
  --orange:#F28A2E;
  --orange-deep:#EE7A1C;
  --teal:#6CC9CF;
  --teal-soft:#E4F5F7;
  --ink:#1B1B1B;
  --body:#4A4A4A;
  --white:#FFFFFF;
  --line:#CFE9EC;
}
*{margin:0;padding:0;box-sizing:border-box}
html,body{width:1200px;height:4594px;overflow:hidden}
body{position:relative;font-family:'Outfit',sans-serif;color:var(--ink);background:var(--white)}
.abs{position:absolute}
.img{position:absolute}
.eyebrow{font-size:16px;letter-spacing:3px;font-weight:500;color:var(--ink);display:flex;align-items:center;gap:10px}
.eyebrow::after{content:"";width:38px;height:1px;background:currentColor;opacity:.6}
.eyebrow.center::before{content:"";width:38px;height:1px;background:currentColor;opacity:.6}
.title{font-size:46px;font-weight:400;line-height:1.12}
.title .hl{color:var(--orange)}
.para{font-size:17.5px;line-height:1.45;color:var(--body);font-weight:300}
.btn{position:absolute;display:flex;align-items:center;justify-content:center;gap:8px;border-radius:0 24px 0 24px;color:var(--white);font-size:15px;font-weight:500;letter-spacing:.5px}
.btn-teal{background:var(--teal)}
.btn-orange{background:var(--orange)}

/* header */
.topbar{left:578px;top:0;width:622px;height:42px;background:var(--teal);border-bottom-left-radius:24px;display:flex;align-items:center;gap:36px;padding-left:30px;color:var(--ink);font-size:14px}
.topbar span{display:flex;align-items:center;gap:8px}
.dot-ic{width:20px;height:20px;border-radius:50%;background:var(--orange);display:inline-flex;align-items:center;justify-content:center}
.brand{left:104px;top:36px;text-align:center}
.brand-name{font-size:42px;font-weight:400;color:#2E4A62;line-height:1}
.brand-sub{font-size:13px;letter-spacing:9px;color:#6A93A6;margin-top:4px}
.nav{left:398px;top:66px;display:flex;gap:44px;font-size:15px;font-weight:500}
.book-top{left:906px;top:57px;width:196px;height:34px;font-size:13px}
.hero-photo{left:520px;top:0;width:680px;height:697px;background:linear-gradient(120deg,#DCEFEA 0%,#B9D6DE 45%,#7FA7C2 100%);border-bottom-right-radius:120px}
.hero-fade{left:0;top:0;width:1200px;height:697px;background:linear-gradient(90deg,#EAF6F4 0%,#EAF6F4 40%,rgba(234,246,244,0) 58%)}
.hero-text{left:110px;top:226px}
.hero-title{font-size:49px;line-height:1.03;font-weight:400;margin-top:14px}
.hero-title .hl{color:var(--orange)}

/* services */
.svc-card{position:absolute;top:888px;width:239px;height:414px;border:1.5px solid var(--teal);border-radius:120px 120px 0 0;text-align:center}
.svc-photo{position:absolute;left:13px;top:12px;width:210px;height:210px;border-radius:50%;border-bottom:4px solid var(--teal)}
.svc-name{position:absolute;left:0;right:0;top:236px;font-size:18.5px;font-weight:500;line-height:1.3}
.svc-text{position:absolute;left:22px;right:22px;top:296px;font-size:13px;line-height:1.5;color:var(--body);font-weight:300}
.svc-card .btn{left:40px;top:348px;width:152px;height:38px;font-size:14px}

/* orange band */
.why{left:0;top:1970px;width:1200px;height:546px;background:linear-gradient(100deg,var(--orange-deep),#F59A45)}
.why-photo{left:618px;top:1970px;width:582px;height:546px;background:linear-gradient(110deg,#C9C2B8,#E6DFD7 60%,#D6CEC6);border-top-left-radius:90px}

/* mission */
.mission{left:0;top:2516px;width:1200px;height:615px;background:linear-gradient(180deg,#E6F5F7,#EDF8F9 70%,#FFFFFF)}

/* testimonials */
.tcard{position:absolute;top:3332px;width:311px;height:260px;background:var(--white);border-radius:0 30px 0 30px;box-shadow:0 4px 24px rgba(0,0,0,.06);padding:44px 34px 0 38px}
.tcard p{font-size:13px;line-height:1.55;color:var(--body);font-weight:300}
.tauth{display:flex;align-items:center;gap:10px;margin-top:28px}
.avatar{width:26px;height:26px;border-radius:50%;background:#B89A86}
.tname{font-size:12px;font-weight:600}
.stars{color:#F5B300;font-size:14px;letter-spacing:1px}

/* appointment */
.appt{left:93px;top:3672px;width:1014px;height:516px;background:var(--teal);overflow:hidden}
.appt-photo{left:0;top:0;width:520px;height:516px;background:linear-gradient(90deg,#D8D2CA,#E8E2DA 55%,rgba(108,201,207,0))}
.field{position:absolute;height:42px;background:var(--white);border:1px solid #D9EFF1;font-size:13px;padding:12px 18px;color:var(--ink)}

/* footer */
.fcol h4{font-size:16px;font-weight:600;margin-bottom:12px}
.fcol h4::after{content:"";display:block;width:135px;height:1px;background:var(--teal);margin-top:10px}
.fcol a{display:block;font-size:14px;color:var(--ink);text-decoration:none;line-height:1.6}
.fc-item{display:flex;gap:14px;align-items:flex-start;font-size:13px;line-height:1.4;margin-bottom:16px}
.fc-ic{width:34px;height:34px;border-radius:50%;background:var(--orange);flex-shrink:0}
.social{width:34px;height:34px;border-radius:50%;background:var(--orange)}
</style>
</head>
<body>

<!-- HERO -->
<div class="img hero-photo" role="img" aria-label="Photo of a smiling senior couple, woman riding piggyback on the man"></div>
<div class="abs hero-fade"></div>
<div class="abs topbar">
  <span><i class="dot-ic"><svg width="11" height="11" viewBox="0 0 24 24"><path fill="#fff" d="M6.6 10.8a15 15 0 0 0 6.6 6.6l2.2-2.2c.3-.3.7-.4 1-.2 1.1.4 2.3.6 3.6.6.6 0 1 .4 1 1V20c0 .6-.4 1-1 1A17 17 0 0 1 3 4c0-.6.4-1 1-1h3.5c.6 0 1 .4 1 1 0 1.3.2 2.5.6 3.6.1.3 0 .7-.2 1z"/></svg></i>24/7 Help (+555) 018 4420</span>
  <span><i class="dot-ic"><svg width="11" height="11" viewBox="0 0 24 24"><circle cx="12" cy="12" r="9" fill="none" stroke="#fff" stroke-width="2.5"/><path d="M12 7v5l3 2" stroke="#fff" stroke-width="2.5" fill="none"/></svg></i>Hours: M-F 8:30 a.m. – 5:00 p.m.</span>
</div>
<div class="abs brand"><div class="brand-name">Nerova Health</div><div class="brand-sub">SERVICES</div></div>
<nav class="abs nav"><span>Home</span><span>About Us</span><span>Services</span><span>Treatment</span><span>Contact Us</span></nav>
<div class="btn btn-orange book-top">Book an Appointment</div>
<div class="abs hero-text">
  <div class="eyebrow">NEROVA HEALTH SERVICES</div>
  <h1 class="hero-title"><span class="hl">Mental Health Care</span><br>Services Provider<br>in Washington</h1>
</div>
<div class="btn btn-teal" style="left:230px;top:443px;width:182px;height:40px;border-radius:0 20px 0 0;font-size:12px;padding-left:40px">LEARN MORE ›</div>
<div class="btn btn-orange" style="left:104px;top:443px;width:176px;height:40px;border-radius:0 20px 0 20px;font-size:12px">BOOK NOW</div>

<!-- SERVICES -->
<div class="abs eyebrow center" style="left:0;width:1200px;top:783px;justify-content:center;font-size:15px">WHAT WE DO</div>
<h2 class="abs title" style="left:0;width:1200px;top:802px;text-align:center"><span class="hl">Services</span> We Offer</h2>

<div class="svc-card" style="left:86px"><div class="img svc-photo" style="background:linear-gradient(135deg,#DCD3CB,#9FB7C8)" role="img" aria-label="Photo of a counseling session between two women"></div><div class="svc-name">Counseling &amp;<br>Psychotherapy</div><div class="svc-text">Lorem ipsum dolor sit amet, consectetur adipiscing</div><div class="btn btn-orange">LEARN MORE ›</div></div>
<div class="svc-card" style="left:350px"><div class="img svc-photo" style="background:linear-gradient(135deg,#CFC7B8,#C99A4A)" role="img" aria-label="Photo of a group therapy conversation"></div><div class="svc-name" style="top:240px">Group Therapy</div><div class="svc-text" style="top:278px">Lorem ipsum dolor sit amet, consectetur adipiscing elit, sed do eiusmod tempor</div><div class="btn btn-orange">LEARN MORE ›</div></div>
<div class="svc-card" style="left:612px"><div class="img svc-photo" style="background:linear-gradient(135deg,#E4E1E4,#A997B8)" role="img" aria-label="Photo of a smiling woman in a consultation"></div><div class="svc-name" style="top:240px">Medication Management</div><div class="svc-text" style="top:278px">Lorem ipsum dolor sit amet, consectetur adipiscing elit, sed do eiusmod tempor</div><div class="btn btn-orange">LEARN MORE ›</div></div>
<div class="svc-card" style="left:875px"><div class="img svc-photo" style="background:linear-gradient(135deg,#BFE2EA,#4E90B5)" role="img" aria-label="Illustration of a glowing brain held in a hand"></div><div class="svc-name">Workplace Mental<br>Health Programs</div><div class="svc-text">Lorem ipsum dolor sit amet, consectetur adipiscin</div><div class="btn btn-orange">LEARN MORE ›</div></div>

<!-- ABOUT -->
<svg class="abs" style="left:52px;top:1375px" width="520" height="520" viewBox="0 0 520 520"><circle cx="260" cy="262" r="252" fill="var(--teal)" opacity=".85"/><path d="M8 262 A252 252 0 0 1 450 95" fill="none" stroke="var(--orange)" stroke-width="14"/></svg>
<div class="img" style="left:126px;top:1414px;width:190px;height:230px;background:linear-gradient(160deg,#E8E4DC,#9A8E7E);border-radius:95px 95px 0 95px" role="img" aria-label="Photo of an elderly woman talking"></div>
<div class="img" style="left:326px;top:1458px;width:220px;height:186px;background:linear-gradient(160deg,#F6E7D2,#D8B28A);border-radius:95px 95px 95px 0" role="img" aria-label="Photo of a laughing woman in a sun hat"></div>
<div class="img" style="left:96px;top:1654px;width:220px;height:186px;background:linear-gradient(160deg,#EDE8E6,#C8A89A);border-radius:95px 0 95px 95px" role="img" aria-label="Photo of hands holding a brain model"></div>
<div class="img" style="left:326px;top:1654px;width:190px;height:230px;background:linear-gradient(160deg,#C8CFC8,#3E5A7A);border-radius:0 95px 95px 95px" role="img" aria-label="Photo of a stressed young woman"></div>

<div class="abs" style="left:628px;top:1446px">
  <div class="eyebrow" style="font-size:15px">WHO WE ARE</div>
  <h2 class="title" style="margin-top:12px"><span class="hl">About</span> Nerova<br>Health Services</h2>
  <p class="para" style="width:490px;margin-top:18px">Lorem ipsum dolor sit amet, consectetur adipiscing elit, sed do eiusmod tempor incididunt ut labore et dolore magna aliqua. Quis ipsum suspendisse ultrices gravida. Risus commodo viverra maecenas accumsan</p>
  <p class="para" style="width:490px;margin-top:22px">Aacus vel facilisis. Lorem ipsum dolor sit amet, consectetur adipiscing elit, sed do eiusmod tempor incididunt ut</p>
</div>
<div class="btn btn-teal" style="left:626px;top:1797px;width:190px;height:50px">LEARN MORE ›</div>

<!-- WHY WE ARE -->
<div class="abs why"></div>
<div class="img why-photo" role="img" aria-label="Photo of a worried young woman holding hands with a therapist"></div>
<div class="abs" style="left:115px;top:2080px;color:#fff">
  <div class="eyebrow" style="color:#fff;font-size:15px">WHY WE ARE</div>
  <h2 class="title" style="color:#fff;margin-top:12px;line-height:1.02">Mental Health<br>Care Therapy</h2>
  <p class="para" style="color:#fff;width:455px;margin-top:12px;font-size:17px;line-height:1.45;font-weight:400">Lorem ipsum dolor sit amet, consectetur adipiscing elit, sed do eiusmod tempor incididunt ut labore et dolore magna aliqua. Quis ipsum suspendisse ultrices gravida. Risus commodo viverra maecenas accumsan Aacus vel facilisis. Lorem ipsum dolor sit amet.</p>
</div>
<div class="btn btn-teal" style="left:114px;top:2362px;width:190px;height:48px">LEARN MORE ›</div>

<!-- MISSION -->
<div class="abs mission"></div>
<div class="abs" style="left:50px;top:2584px;width:76px;height:76px;border-radius:50%;background:var(--teal)"></div>
<div class="img" style="left:80px;top:2566px;width:254px;height:388px;background:linear-gradient(160deg,#E7DDCF,#A9B4C2);border-radius:127px 127px 0 0" role="img" aria-label="Photo of a male therapist with glasses gesturing"></div>
<div class="img" style="left:346px;top:2674px;width:254px;height:386px;background:linear-gradient(160deg,#9DAA78,#D8B392 60%,#7E9A6A);border-radius:0 0 127px 127px" role="img" aria-label="Photo of a laughing couple embracing"></div>
<div class="abs" style="left:663px;top:2636px">
  <div class="eyebrow" style="font-size:15px">WHY US?</div>
  <h2 class="title" style="margin-top:12px"><span class="hl">Our</span> Mission</h2>
  <p class="para" style="width:470px;margin-top:18px">Lorem ipsum dolor sit amet, consectetur adipiscing elit, sed do eiusmod tempor incididunt ut labore et dolore magna aliqua. Quis ipsum suspendisse ultrices gravida. Risus commodo viverra maecenas accumsan</p>
  <p class="para" style="width:470px;margin-top:22px">Aacus vel facilisis. Lorem ipsum dolor sit amet, consectetur adipiscing elit, sed do eiusmod tempor incididunt ut</p>
</div>
<div class="btn btn-teal" style="left:664px;top:2938px;width:190px;height:50px">LEARN MORE ›</div>

<!-- TESTIMONIALS -->
<div class="abs" style="left:0;top:3131px;width:1200px;height:540px;background:linear-gradient(90deg,#FFFFFF 60%,#FDEBDC)"></div>
<div class="abs eyebrow center" style="left:0;width:1200px;top:3217px;justify-content:center;font-size:15px">TESTIMONIALS</div>
<h2 class="abs title" style="left:0;width:1200px;top:3236px;text-align:center"><span class="hl">What</span> Patient Says</h2>
<svg class="abs" style="left:58px;top:3454px" width="18" height="28" viewBox="0 0 18 28"><path d="M14 3 4 14l10 11" stroke="var(--orange)" stroke-width="3" fill="none"/></svg>
<svg class="abs" style="left:1126px;top:3454px" width="18" height="28" viewBox="0 0 18 28"><path d="m4 3 10 11-10 11" stroke="var(--orange)" stroke-width="3" fill="none"/></svg>
<div class="tcard" style="left:102px"><p>Lorem ipsum dolor sit amet, consectetur adipiscing elit, sed do eiusmod tempor incididunt ut labore et dolore magna aliqua. Ut enim ad minim veniam, quis nostrud exercitation ullamco laboris nisi ut aliquip</p><div class="tauth"><span class="avatar"></span><div><div class="tname">Omar T.</div><div class="stars">★★★★★</div></div></div></div>
<div class="tcard" style="left:443px"><p>Lorem ipsum dolor sit amet, consectetur adipiscing elit, sed do eiusmod tempor incididunt ut labore et dolore magna aliqua. Ut enim ad minim veniam, quis nostrud exercitation ullamco laboris nisi ut aliquip</p><div class="tauth"><span class="avatar"></span><div><div class="tname">Lena P.</div><div class="stars">★★★★★</div></div></div></div>
<div class="tcard" style="left:784px"><p>Lorem ipsum dolor sit amet, consectetur adipiscing elit, sed do eiusmod tempor incididunt ut labore et dolore magna aliqua. Ut enim ad minim veniam, quis nostrud exercitation ullamco laboris nisi ut aliquip</p><div class="tauth"><span class="avatar"></span><div><div class="tname">Rhea Vance</div><div class="stars">★★★★★</div></div></div></div>

<!-- APPOINTMENT -->
<div class="abs appt">
  <div class="img appt-photo" role="img" aria-label="Photo of a smiling woman at a doctor's office"></div>
  <div class="abs" style="left:487px;top:80px;color:#fff">
    <div class="eyebrow" style="color:#fff;font-size:15px">GET IN TOUCH</div>
    <h2 class="title" style="color:#fff;font-size:38px;margin-top:6px">Book an Appointment</h2>
  </div>
  <div class="field" style="left:487px;top:166px;width:220px">First Name</div>
  <div class="field" style="left:715px;top:166px;width:200px">Last Name</div>
  <div class="field" style="left:487px;top:220px;width:220px">Email address</div>
  <div class="field" style="left:715px;top:220px;width:200px">Phone number</div>
  <div class="field" style="left:487px;top:274px;width:428px;height:104px">Message</div>
  <div class="btn btn-orange" style="left:487px;top:396px;width:178px;height:42px;border-radius:21px;font-size:14px">SEND MESSAGE</div>
</div>

<!-- FOOTER -->
<div class="abs brand" style="left:134px;top:4268px"><div class="brand-name">Nerova Health</div><div class="brand-sub">SERVICES</div></div>
<div class="abs" style="left:180px;top:4354px;display:flex;gap:18px"><span class="social"></span><span class="social"></span><span class="social"></span></div>
<div class="abs fcol" style="left:475px;top:4270px"><h4>NAVIGATION</h4><a>About us</a><a>Why Us</a><a>Services</a><a>Mental Care Therapy</a><a>Contact</a></div>
<div class="abs fcol" style="left:674px;top:4270px"><h4>RESOURCES</h4><a>FAQ</a><a>Testimonials</a><a>Career</a><a>Book appointment</a><a>Contact</a></div>
<div class="abs fcol" style="left:872px;top:4270px"><h4>CONTACT US</h4>
  <div class="fc-item" style="margin-top:6px"><span class="fc-ic"></span><div>Phone Number<br>(555) 014-2768</div></div>
  <div class="fc-item"><span class="fc-ic"></span><div>4821 Larkfield Lane, Suite 12,<br>Ashbury, IL 60000</div></div>
  <div class="fc-item"><span class="fc-ic"></span><div>Hours:<br>M-F 8:30 a.m. – 5:00 p.m.</div></div>
</div>
<div class="abs" style="left:0;top:4510px;width:1200px;height:1px;background:var(--line)"></div>
<div class="abs" style="left:0;width:1200px;top:4544px;text-align:center;font-size:13px">© 2025 <u>Nerova Health Services</u>. All Rights Reserved</div>

</body>
</html>
```